Get Up to $ 500,000 in Business Capital within 48 hours

design a flyer offering business capital to businesses. The flyer is going to be mailed to business owners and the flyer needs to immediately capture their attention.
The flyer needs to be bold and professional and really stand-out.
pppppppppppppppppppppppppppppppppppppppppppppppppppppppppppppppppppppppppppppppppppppppppppppppppppppppppppppppppppppppppppppppppppppppppppppppppppppppppppppppppppppppppppppppppppppppppppppppppppppppppppppppppppppppppppppppppppppp

Target Market(s)

business owners

Font styles to use
Serif

Requirements
Must have
• Apply online in minutes at MorvelCapital.com or call 800-TAKE-NOW
Nice to have
• We fund almost every business type. Not a business loan, receive a cash advance on your future sales.

```html
<!DOCTYPE html>
<html lang="en">
<head>
<meta charset="utf-8">
<title>MorvelCapital – Business Capital Flyer</title>
<link href="https://fonts.googleapis.com/css2?family=Archivo+Black&family=Montserrat:wght@500;600;700;800&display=swap" rel="stylesheet">
<style>
  :root{
    --navy:#233a8b;
    --navy-deep:#1f3384;
    --sky:#2f9ad6;
    --sky-light:#3aa6dc;
    --ink:#1d1d22;
    --paper:#f4f4f5;
    --white:#ffffff;
    --backdrop:#e6e8eb;
    --leaf:#4caf50;
    --leaf-light:#c9e3a8;
  }
  *{box-sizing:border-box;margin:0;padding:0}
  html,body{width:1200px;height:900px;overflow:hidden;background:var(--backdrop)}
  .flyer{position:absolute;left:40px;top:90px;width:1120px;height:720px;overflow:hidden;background:var(--paper);box-shadow:0 6px 22px rgba(0,0,0,.18);font-family:"Montserrat",Arial,sans-serif}
  .hero-photo{position:absolute;inset:0;background:
      radial-gradient(circle at 75% 30%, #e8f1c8 0%, rgba(232,241,200,0) 35%),
      radial-gradient(circle at 60% 70%, #d9c3ad 0%, rgba(217,195,173,0) 30%),
      linear-gradient(120deg, #dfeede 30%, var(--leaf-light) 50%, #7cc46a 75%, var(--leaf) 100%)}
  .panel-shapes{position:absolute;inset:0}
  .brand{position:absolute;left:44px;top:44px;font-weight:800;font-size:44px;letter-spacing:.5px;color:var(--navy);line-height:1;white-space:nowrap}
  .headline{position:absolute;left:58px;top:152px;font-family:"Archivo Black",Impact,sans-serif;font-weight:400;font-size:35px;color:var(--white);line-height:1;white-space:nowrap}
  .offer{position:absolute;left:100px;top:230px;font-weight:800;font-size:24px;color:var(--ink);line-height:1.25;white-space:nowrap}
  .offer em{font-style:normal;color:var(--navy)}
  .perks{position:absolute;left:100px;top:316px;list-style:none}
  .perks li{display:flex;align-items:center;gap:16px;font-weight:700;font-size:18px;color:var(--ink);height:48px;white-space:nowrap}
  .perk-icon{width:40px;height:40px;flex:none}
  .benefits{position:absolute;left:180px;top:456px;list-style:none}
  .benefits li{display:flex;align-items:flex-start;gap:12px;font-weight:700;font-size:16px;color:var(--white);line-height:1.25;margin-bottom:14px;white-space:nowrap}
  .tick{width:24px;height:24px;flex:none}
  .cta{position:absolute;left:180px;top:624px;font-weight:700;font-size:22px;color:var(--ink);line-height:1.2;white-space:nowrap}
  .cta .link{color:var(--navy);font-weight:600}
</style>
</head>
<body>
<main class="flyer">
  <div class="hero-photo" role="img" aria-label="Photo: adult hands passing a glass jar of coins with a green sprout to a child's open hands, soft green bokeh background"></div>

  <svg class="panel-shapes" width="1120" height="720" viewBox="0 0 1120 720">
    <defs>
      <linearGradient id="band" x1="0" y1="0" x2="1" y2="0">
        <stop offset="0" stop-color="var(--navy-deep)"/>
        <stop offset="1" stop-color="var(--sky)"/>
      </linearGradient>
      <linearGradient id="block" x1="0" y1="1" x2="1" y2="0">
        <stop offset="0" stop-color="var(--navy-deep)"/>
        <stop offset="1" stop-color="var(--sky-light)"/>
      </linearGradient>
    </defs>
    <polygon points="0,0 540,0 670,720 0,720" fill="var(--paper)"/>
    <polygon points="40,130 556,130 571,212 40,212" fill="url(#band)"/>
    <polygon points="150,440 612,440 644,612 150,612" fill="url(#block)"/>
    <polygon points="532,0 548,0 678,720 662,720" fill="var(--sky)"/>
  </svg>

  <div class="brand">MORVELCAPITAL</div>
  <h1 class="headline">Need business capital?</h1>
  <p class="offer">You can qualify for up to <em>500,000</em><br>in just <em>24 hours.</em></p>

  <ul class="perks">
    <li>
      <svg class="perk-icon" viewBox="0 0 40 40"><circle cx="20" cy="20" r="19" fill="var(--sky)" stroke="var(--navy)" stroke-width="2"/><circle cx="20" cy="16" r="7" fill="none" stroke="#fff" stroke-width="2"/><text x="20" y="20" text-anchor="middle" font-size="10" font-weight="700" fill="#fff" font-family="Montserrat,sans-serif">$</text><path d="M9 28h8l6 2h8" fill="none" stroke="#fff" stroke-width="2"/></svg>
      No minimum credit score
    </li>
    <li>
      <svg class="perk-icon" viewBox="0 0 40 40"><circle cx="20" cy="20" r="19" fill="var(--sky)" stroke="var(--navy)" stroke-width="2"/><rect x="12" y="10" width="14" height="19" fill="none" stroke="#fff" stroke-width="2"/><path d="M15 15h8M15 19h8M15 23h5M24 27l6-6" stroke="#fff" stroke-width="2"/></svg>
      Simple 1 page application
    </li>
  </ul>

  <ul class="benefits">
    <li><svg class="tick" viewBox="0 0 24 24"><circle cx="12" cy="12" r="10" fill="none" stroke="#fff" stroke-width="2"/><path d="M7 12l4 4 8-10" fill="none" stroke="#fff" stroke-width="2.6"/></svg><span>Not a business loan, get a cash advance<br>today on your future sales.</span></li>
    <li><svg class="tick" viewBox="0 0 24 24"><circle cx="12" cy="12" r="10" fill="none" stroke="#fff" stroke-width="2"/><path d="M7 12l4 4 8-10" fill="none" stroke="#fff" stroke-width="2.6"/></svg><span>Convenient alternative to a bank loan.</span></li>
    <li><svg class="tick" viewBox="0 0 24 24"><circle cx="12" cy="12" r="10" fill="none" stroke="#fff" stroke-width="2"/><path d="M7 12l4 4 8-10" fill="none" stroke="#fff" stroke-width="2.6"/></svg><span>We fund virtually every type of business.</span></li>
  </ul>

  <p class="cta">Apply in minutes online at<br><span class="link">MorvelCapital.com</span> or<br>call <span class="link">1-800-TAKE-NOW</span></p>
</main>
</body>
</html>
```